Two-page Website Design for Construction Business

Make a one or two-page website. (Two-page if it is better to put "contact us" on separate page.
Must be cell phone responsive.
Needs to be posted to brivantohost.com.
Some minor graphic design is required.
Sample layout is provided in ppt file.
All content is provided in ppt file except the graphics need to be professionally made.
Reason: Only 3 designers competing for this simple site. I will extend for 5 days.
Suggested photos from lumafrond:
Storefront: 144849883
Industrial: 139927951
ADA: 282622679
Ballistic: 311146781 or 652211317
Corrosion: 465155321
Clean room: 478585840
Hurricane: 110081945 or 127898684
Fire: 271704542
Chemical: 242308249 or 93390571
Target Market(s)
Construction
Industry/Entity Type
Construction
Coding
Coded - Design and coding required
Number of Pages Required
2 page
Colors
Designer to choose colors to be used in the design.
Requirements
Must have
- I'm not sure what "uncoded" means, but the site must be loaded to brivantohost.com and it must be operational.
- Please use standard error checking such as only numbers for phone info, correctly formatted email addresses, etc.
- I must be able to update the site easily -- wordpress.

```html
<!DOCTYPE html>
<html lang="en">
<head>
<meta charset="utf-8">
<title>Ridgeline Entryways – Commercial Door Installation &amp; Repair</title>
<link rel="stylesheet" href="https://fonts.googleapis.com/css2?family=Cinzel:wght@700;900&family=Lato:wght@400;700;900&family=Alegreya:wght@500&display=swap">
<style>
:root{
  --navy:#2c3a92;
  --red:#e61c24;
  --white:#ffffff;
  --field:#f3f3f3;
  --panel-grey:#efefef;
  --text:#333333;
}
*{box-sizing:border-box;margin:0;padding:0}
html,body{width:1200px;height:2466px;overflow:hidden}
body{position:relative;background:var(--white);font-family:"Lato",sans-serif;color:var(--text)}
.abs{position:absolute}

/* header */
.site-header{left:0;top:0;width:1200px;height:105px;background:var(--white)}
.brand{display:flex;align-items:center;gap:12px}
.brand-mark{width:30px;height:30px;background:var(--red)}
.brand-name{font-weight:900;font-size:32px;color:var(--navy);line-height:1;white-space:nowrap}
.brand-tag{font-size:14px;color:var(--navy);margin-top:4px;margin-left:42px;white-space:nowrap}
.header-brand{left:79px;top:22px}
.main-nav{left:480px;top:44px;display:flex;gap:28px;font-size:14px;color:#b8b8b8}
.main-nav .active{color:var(--navy);font-weight:700}
.nav-divider{left:1076px;top:34px;width:2px;height:38px;background:var(--navy)}
.search-icon{left:1090px;top:44px}

/* hero */
.hero-photo{left:0;top:105px;width:1200px;height:690px;
  background:linear-gradient(120deg,#e9eef1 0%,#f7f9fa 35%,#c9d3d9 70%,#9aa7b0 100%);
  clip-path:polygon(0 0,100% 0,100% 100%,60% 91%,0 86%)}
.hero-title{left:72px;top:300px;font-family:"Cinzel",serif;font-weight:900;font-size:42px;line-height:48px;color:var(--navy);letter-spacing:1px}
.hero-lead{left:72px;top:406px;width:500px;font-size:17px;line-height:22px;color:#444}
.hero-area{left:72px;top:472px;font-size:21px;font-weight:700;color:var(--red)}

/* contact cards */
.contact-card{top:735px;width:313px;height:187px;background:var(--red);color:var(--white);text-align:center}
.card-phone{left:77px}
.card-mail{left:810px}
.card-icon{left:104px;top:-50px;width:108px;height:108px;border-radius:50%;background:var(--navy);border:7px solid #d9d9d9;display:flex;align-items:center;justify-content:center}
.card-lines{position:absolute;left:0;right:0;top:72px;font-size:24px;font-weight:700;line-height:33px}
.card-btn{top:896px;width:209px;height:53px;background:var(--navy);color:var(--white);font-size:18px;font-weight:700;display:flex;align-items:center;justify-content:center}

/* quote form */
.quote-box{left:423px;top:679px;width:355px;height:437px;background:var(--white);border-radius:6px;box-shadow:0 4px 18px rgba(0,0,0,.18)}
.quote-title{left:0;width:355px;top:26px;text-align:center;font-family:"Cinzel",serif;font-weight:700;font-size:28px;color:var(--red)}
.quote-field{left:32px;width:290px;height:43px;background:var(--field);font-size:13px;color:#777;padding:13px 22px}
.btn-submit{left:73px;top:339px;width:208px;height:52px;background:var(--navy);color:var(--white);font-size:18px;font-weight:700;display:flex;align-items:center;justify-content:center}

/* about */
.about-band{left:0;top:1018px;width:1200px;height:347px;background:var(--navy)}
.about-title{left:0;width:1200px;top:1148px;text-align:center;font-family:"Alegreya",serif;font-size:54px;color:var(--white)}
.about-title .accent{color:var(--red)}
.about-text{left:120px;width:960px;top:1230px;text-align:center;font-size:13px;line-height:20px;color:#8f98cc}
.speciality{width:140px;text-align:center}
.speciality-icon{width:84px;height:84px;border-radius:50%;background:var(--navy);border:6px solid #d4d4d4;margin:0 auto}
.speciality-label{font-size:18px;color:#222;margin-top:14px}
.speciality.current .speciality-label{color:var(--red)}

/* mid brand */
.mid-brand{left:0;width:1200px;top:1500px;display:flex;justify-content:center}
.mid-brand .brand-name{font-size:40px}
.mid-brand .brand-mark{width:36px;height:36px}
.mid-brand .brand-tag{font-size:17px;margin-left:48px}

/* feature panels */
.feature{top:1621px;width:400px;height:312px;text-align:center}
.feature-grey{background:var(--panel-grey)}
.feature-red{background:var(--red)}
.feature-icon{position:absolute;left:0;right:0;top:50px;display:flex;justify-content:center}
.feature-title{position:absolute;left:0;right:0;top:148px;font-size:22px;letter-spacing:1px;color:#222}
.feature-red .feature-title{color:var(--white);top:142px}
.feature-btn{position:absolute;left:106px;top:201px;width:188px;height:50px;background:var(--navy);color:var(--white);font-size:18px;font-weight:700;display:flex;align-items:center;justify-content:center}
.feature-red .feature-btn{background:var(--white);color:var(--red)}

/* contact section */
.contact-section{left:0;top:1933px;width:1200px;height:470px;background:linear-gradient(180deg,#4a57a8 0%,#3b4aa0 55%,#46509c 100%)}
.contact-title{left:0;width:1200px;top:1978px;text-align:center;font-family:"Alegreya",serif;font-size:52px;color:var(--white)}
.contact-title .accent{color:var(--red)}
.inquiry-label{left:79px;top:2058px;font-size:18px;font-weight:700;color:var(--white);letter-spacing:.5px}
.inquiry-label span{font-weight:400}
.inquiry-field{height:41px;background:var(--field);border-radius:3px;font-size:12px;color:#999;padding:13px 14px}
.inquiry-message{left:77px;top:2163px;width:697px;height:147px;padding:14px}
.send-btn{left:640px;top:2266px;width:82px;height:82px;border-radius:50%;background:var(--navy);border:6px solid #d9d9d9;display:flex;align-items:center;justify-content:center}
.info-col{left:835px;width:240px;top:2058px;text-align:center;color:var(--white)}
.info-title{font-size:20px;font-weight:700;letter-spacing:1px}
.info-item{font-size:14px;line-height:21px}

/* footer */
.site-footer{left:0;top:2403px;width:1200px;height:63px;background:var(--red)}
.footer-copy{left:79px;top:2424px;font-size:14px;color:var(--white)}
.footer-copy strong{font-size:17px}
.footer-copy .sep{margin:0 12px}
.social{top:2413px;width:42px;height:42px;border-radius:50%;border:2px solid var(--white)}
</style>
</head>
<body>

<header class="abs site-header">
  <div class="abs header-brand">
    <div class="brand"><span class="brand-mark"></span><span class="brand-name">Ridgeline Entryways</span></div>
    <div class="brand-tag">Commercial Door Installation &amp; Repair</div>
  </div>
  <nav class="abs main-nav">
    <span class="active">Home</span><span>Speciality</span><span>Services</span><span>Why us</span><span>Terms</span><span>Quote or service</span><span>Contact</span>
  </nav>
  <div class="abs nav-divider"></div>
  <svg class="abs search-icon" width="18" height="18" viewBox="0 0 18 18"><circle cx="7" cy="7" r="5" fill="none" stroke="#e61c24" stroke-width="2.5"/><line x1="11" y1="11" x2="16" y2="16" stroke="#e61c24" stroke-width="2.5"/></svg>
</header>

<div class="abs hero-photo" role="img" aria-label="Bright modern office with glass partitions, white sculpted wall and a yellow lounge chair"></div>
<h1 class="abs hero-title">COMMERCIAL DOOR<br>INSTALLATION &amp; REPAIR</h1>
<p class="abs hero-lead">Your First and Only Call!! If we don't provide it, install it, or repair it, we'll recommend a great company that will</p>
<p class="abs hero-area">Proudly serving Houston and the surrounding areas</p>

<div class="abs contact-card card-phone">
  <div class="abs card-icon"><svg width="46" height="46" viewBox="0 0 46 46"><circle cx="23" cy="23" r="21" fill="none" stroke="#fff" stroke-width="2"/><path d="M16 12c2-1 4 3 5 5s-2 3-2 4 3 6 6 7 2-2 4-2 5 3 4 5-3 3-5 3c-8 0-15-9-15-16 0-2 1-5 3-6z" fill="#fff"/></svg></div>
  <div class="card-lines">Wade : 555-210-4831<br>Curtis : 555-376-0192</div>
</div>
<div class="abs card-btn" style="left:130px">Same Day Responce</div>

<div class="abs contact-card card-mail">
  <div class="abs card-icon"><svg width="50" height="36" viewBox="0 0 50 36"><rect x="2" y="2" width="46" height="32" fill="none" stroke="#fff" stroke-width="2.5"/><path d="M2 2l23 18L48 2M2 34l17-15M48 34L31 19" fill="none" stroke="#fff" stroke-width="2.5"/></svg></div>
  <div class="card-lines">Email :<br>info@ridgelineentry.com</div>
</div>
<div class="abs card-btn" style="left:862px">Next Day Responce</div>

<div class="abs about-band"></div>

<form class="abs quote-box">
  <div class="abs quote-title">NEED A QUOTE?</div>
  <div class="abs quote-field" style="top:84px">Name:</div>
  <div class="abs quote-field" style="top:130px">Mobile Phone:</div>
  <div class="abs quote-field" style="top:177px">Email:</div>
  <div class="abs quote-field" style="top:225px;height:112px">Message:</div>
  <div class="abs btn-submit">Submit</div>
</form>

<h2 class="abs about-title"><span class="accent">About</span> Ridgeline Entryways</h2>
<p class="abs about-text">Ridgeline Entryways has supplied, installed and serviced commercial doors across the Houston region for many years. Our crews handle storefront, industrial, ADA, cleanroom, ballistic, hurricane, chemical, fire and corrosion resistant openings, with fast response, honest pricing and careful work that keeps your building secure, compliant and open for business every single day.</p>

<div class="abs speciality current" style="left:63px;top:1323px"><div class="speciality-icon"></div><div class="speciality-label">Storefront</div></div>
<div class="abs speciality" style="left:180px;top:1323px"><div class="speciality-icon"></div><div class="speciality-label">Industrial</div></div>
<div class="abs speciality" style="left:297px;top:1323px"><div class="speciality-icon"></div><div class="speciality-label">ADA</div></div>
<div class="abs speciality" style="left:413px;top:1323px"><div class="speciality-icon"></div><div class="speciality-label">Cleanroom</div></div>
<div class="abs speciality" style="left:530px;top:1323px"><div class="speciality-icon"></div><div class="speciality-label">Ballistic</div></div>
<div class="abs speciality" style="left:647px;top:1323px"><div class="speciality-icon"></div><div class="speciality-label">Hurricane</div></div>
<div class="abs speciality" style="left:764px;top:1323px"><div class="speciality-icon"></div><div class="speciality-label">Chemical</div></div>
<div class="abs speciality" style="left:880px;top:1323px"><div class="speciality-icon"></div><div class="speciality-label">Fire</div></div>
<div class="abs speciality" style="left:997px;top:1323px"><div class="speciality-icon"></div><div class="speciality-label">Corrosion</div></div>

<div class="abs mid-brand">
  <div>
    <div class="brand"><span class="brand-mark"></span><span class="brand-name">Ridgeline Entryways</span></div>
    <div class="brand-tag">Commercial Door Installation &amp; Repair</div>
  </div>
</div>

<section class="abs feature feature-grey" style="left:0">
  <div class="feature-icon"><svg width="80" height="80" viewBox="0 0 80 80"><path d="M14 38h12v32H14zM30 40l12-22c2-4 8-3 8 2l-2 14h18c4 0 6 4 5 7l-6 24c-1 3-3 5-6 5H30z" fill="#fff" stroke="#555" stroke-width="3" stroke-linejoin="round"/></svg></div>
  <div class="feature-title">SPECIALITIES</div>
  <div class="feature-btn">Click to see</div>
</section>
<section class="abs feature feature-red" style="left:400px">
  <div class="feature-icon"><svg width="96" height="80" viewBox="0 0 96 80"><g fill="#fff"><circle cx="34" cy="34" r="18"/><g stroke="#fff" stroke-width="9"><line x1="34" y1="8" x2="34" y2="60"/><line x1="8" y1="34" x2="60" y2="34"/><line x1="16" y1="16" x2="52" y2="52"/><line x1="52" y1="16" x2="16" y2="52"/></g><circle cx="66" cy="58" r="11"/><g stroke="#fff" stroke-width="6"><line x1="66" y1="42" x2="66" y2="74"/><line x1="50" y1="58" x2="82" y2="58"/><line x1="55" y1="47" x2="77" y2="69"/><line x1="77" y1="47" x2="55" y2="69"/></g><circle cx="70" cy="18" r="9"/><g stroke="#fff" stroke-width="5"><line x1="70" y1="5" x2="70" y2="31"/><line x1="57" y1="18" x2="83" y2="18"/></g></g><circle cx="34" cy="34" r="7" fill="#e61c24"/><circle cx="66" cy="58" r="4" fill="#e61c24"/><circle cx="70" cy="18" r="3" fill="#e61c24"/></svg></div>
  <div class="feature-title">SERVICES</div>
  <div class="feature-btn">Click to see</div>
</section>
<section class="abs feature feature-grey" style="left:800px">
  <div class="feature-icon"><svg width="84" height="84" viewBox="0 0 84 84"><circle cx="42" cy="42" r="38" fill="#fff" stroke="#777" stroke-width="5"/><path d="M30 32c0-8 6-12 12-12s12 4 12 11c0 9-10 9-10 18v3" fill="none" stroke="#777" stroke-width="7" stroke-linecap="round"/><circle cx="44" cy="63" r="4.5" fill="#777"/></svg></div>
  <div class="feature-title">WHY US</div>
  <div class="feature-btn">Click to see</div>
</section>

<section class="abs contact-section" role="img" aria-label="Company storefront and service van photo tinted blue"></section>
<h2 class="abs contact-title"><span class="accent">Contact</span> Us</h2>
<div class="abs inquiry-label">INQUIRY FORM <span>– Request a Quote or Send Us a Message</span></div>
<div class="abs inquiry-field" style="left:77px;top:2101px;width:219px">Name</div>
<div class="abs inquiry-field" style="left:317px;top:2101px;width:219px">E-Mail</div>
<div class="abs inquiry-field" style="left:556px;top:2101px;width:218px">Subject</div>
<div class="abs inquiry-field inquiry-message">Message</div>
<div class="abs send-btn"><svg width="30" height="22" viewBox="0 0 30 22"><rect x="1" y="1" width="28" height="20" fill="none" stroke="#fff" stroke-width="2"/><path d="M1 1l14 11L29 1" fill="none" stroke="#fff" stroke-width="2"/></svg></div>

<div class="abs info-col">
  <div class="info-title">CONTACT INFO</div>
  <svg style="margin-top:18px" width="24" height="32" viewBox="0 0 24 32"><path d="M12 30C4 19 2 15 2 11a10 10 0 0 1 20 0c0 4-2 8-10 19z" fill="none" stroke="#fff" stroke-width="2"/><circle cx="12" cy="11" r="4" fill="none" stroke="#fff" stroke-width="2"/></svg>
  <div class="info-item">P.O. Box 4821<br>Harlow, TX 77590</div>
  <svg style="margin-top:14px" width="30" height="30" viewBox="0 0 30 30"><path d="M6 3c2-1 5 4 6 6s-2 3-2 4 4 7 7 8 2-2 4-2 6 4 5 6-3 3-5 3C12 28 3 18 3 9c0-3 1-5 3-6z" fill="none" stroke="#fff" stroke-width="2"/></svg>
  <div class="info-item">Wade : 555-210-4831<br>Curtis : 555-376-0192</div>
  <svg style="margin-top:12px" width="30" height="20" viewBox="0 0 30 20"><rect x="1" y="1" width="28" height="18" fill="none" stroke="#fff" stroke-width="2"/><path d="M1 1l14 10L29 1" fill="none" stroke="#fff" stroke-width="2"/></svg>
  <div class="info-item">info@ridgelineentry.com</div>
</div>

<footer class="abs site-footer"></footer>
<div class="abs footer-copy">© <strong>Ridgeline Entryways</strong> - 2017. All Rights Reserved. SITEMAP<span class="sep">|</span><strong style="font-size:14px">TERMS &amp; CONDITIONS</strong></div>
<div class="abs social" style="left:873px"></div>
<div class="abs social" style="left:924px"></div>
<div class="abs social" style="left:977px"></div>
<div class="abs social" style="left:1028px"></div>
<div class="abs social" style="left:1080px"></div>

</body>
</html>
```